Flyer Tally Your Ledger Free

Hi
Can you please design me a DL Flyer for: Tally Your Ledger Free
Info:
Starting a new Business ?
Want to save on bookkeeping fees for your existing business?

You can now save 1000's off bookkeeping fees by Doing it Yourself.

Using our Bookkeeper software you simply key in the information as you go.

We offer one on one training, backup and support.
We can assist you with BAS Preparation and Payrol Advice.

Add Modules as required:
Point of Sale Module
Jobs Management Module
Website Intergration Module

Fee set up assistance and training.

Lets get the ball rolling: 1300 642 815
www.tylfr.com.au
admin@tylfr.com.au (use the logo thing you made)

Target Market(s)

Small Business

Colors
ec1f27
f04a50
f59296
fcdcdc
ffffff

Requirements
Nice to have
• image/s related to bookkeeping

```html
<!DOCTYPE html>
<html lang="en">
<head>
<meta charset="utf-8">
<title>Tally Your Ledger Free – DL Flyer</title>
<link href="https://fonts.googleapis.com/css2?family=Montserrat:wght@400;600;800;900&family=Roboto:wght@400;500;700&display=swap" rel="stylesheet">
<style>
  :root {
    --red: #ec1f27;
    --red-deep: #c4121c;
    --red-band: #a3000d;
    --red-soft: #f04a50;
    --pink: #fcdcdc;
    --yellow: #ffe600;
    --sky: #e2eefb;
    --ink: #111111;
    --grey: #444444;
    --white: #ffffff;
    --backdrop: #2a0005;
  }
  * { box-sizing: border-box; margin: 0; padding: 0; }
  html, body { width: 1200px; height: 857px; overflow: hidden; }
  body { background: var(--backdrop); font-family: "Roboto", Arial, sans-serif; position: relative; }

  .flyer {
    position: absolute; left: 416px; top: 38px;
    width: 368px; height: 780px; overflow: hidden;
    background: var(--sky);
  }

  .hero {
    position: absolute; left: 0; top: 0; width: 368px; height: 274px;
    background: linear-gradient(160deg, var(--red) 0%, var(--red-deep) 100%);
  }
  .hero-photo {
    position: absolute; right: 0; top: 8px; width: 184px; height: 266px;
    background: radial-gradient(ellipse at 55% 40%, #6b5a55 0%, #2f3e63 45%, rgba(150,20,30,0) 80%);
  }
  .hero-title {
    position: absolute; left: 24px; top: 44px;
    font-family: "Montserrat", Arial, sans-serif; font-weight: 900;
    font-size: 27px; line-height: 27px; color: var(--yellow);
  }
  .hero-sub {
    position: absolute; left: 24px; top: 141px; width: 140px;
    font-family: "Montserrat", Arial, sans-serif; font-weight: 400;
    font-size: 13.5px; line-height: 19px; color: var(--white); letter-spacing: .3px;
  }

  .brand-arc { position: absolute; left: 0; top: 274px; width: 368px; height: 82px; }
  .brand {
    position: absolute; left: 0; top: 288px; width: 368px;
    display: flex; justify-content: center; align-items: center; gap: 7px;
  }
  .brand-dot { width: 18px; height: 18px; border-radius: 50%; background: var(--red); }
  .brand-name {
    font-family: "Montserrat", Arial, sans-serif; font-weight: 600;
    font-size: 18px; color: var(--red);
  }

  .offer-frame {
    position: absolute; left: 42px; top: 381px; width: 292px; height: 51px;
    border: 1.2px solid var(--red);
  }
  .offer-lead, .offer-headline, .offer-tail {
    position: absolute; left: 0; width: 368px; text-align: center;
  }
  .offer-lead { top: 369px; font-size: 14px; color: var(--ink); }
  .offer-lead span, .offer-tail span { background: var(--sky); padding: 0 8px; }
  .offer-headline {
    top: 389px; font-family: "Montserrat", Arial, sans-serif; font-weight: 900;
    font-size: 27px; line-height: 30px; color: var(--red); letter-spacing: -.3px;
  }
  .offer-tail { top: 420px; font-size: 14px; color: var(--ink); }

  .details {
    position: absolute; left: 0; top: 451px; width: 368px; text-align: center;
    font-size: 10px; line-height: 15.5px; color: var(--ink);
  }
  .details p + p { margin-top: 2px; }

  .modules {
    position: absolute; left: 15px; top: 525px; width: 338px; height: 99px;
    background: var(--red);
  }
  .modules-title {
    position: absolute; left: 0; top: 7px; width: 100%; text-align: center;
    font-family: "Montserrat", Arial, sans-serif; font-weight: 800;
    font-size: 15px; color: var(--yellow);
  }
  .module {
    position: absolute; top: 32px; width: 101px; height: 59px; background: var(--white);
    display: flex; align-items: center; justify-content: center; text-align: center;
    font-weight: 700; font-size: 9.5px; line-height: 12.5px; color: var(--ink); letter-spacing: .3px;
  }
  .module-pos { left: 10px; }
  .module-jobs { left: 118px; }
  .module-web { left: 226px; }

  .setup {
    position: absolute; left: 0; top: 631px; width: 368px; text-align: center;
    font-family: "Montserrat", Arial, sans-serif; font-weight: 900;
    font-size: 17px; line-height: 21px; color: var(--ink);
  }
  .setup-cta {
    position: absolute; left: 0; top: 681px; width: 368px; text-align: center;
    font-size: 10px; letter-spacing: 1px; color: var(--grey);
  }

  .contact-band {
    position: absolute; left: 0; top: 701px; width: 368px; height: 79px;
    background: var(--red-band);
  }
  .phone {
    position: absolute; left: 0; top: 12px; width: 100%;
    display: flex; justify-content: center; align-items: center; gap: 6px;
    font-weight: 700; font-size: 36px; color: var(--white); letter-spacing: .5px;
  }
  .links {
    position: absolute; left: 0; top: 55px; width: 100%;
    display: flex; justify-content: center; gap: 14px;
    font-weight: 700; font-size: 10px; color: var(--white);
  }
  .links span { display: flex; align-items: center; gap: 3px; }
</style>
</head>
<body>
<div class="flyer">
  <section class="hero">
    <div class="hero-photo" role="img" aria-label="Photo of a thoughtful businessman in a navy suit holding a tablet"></div>
    <h1 class="hero-title">STARTING<br>A NEW<br>BUSINESS?</h1>
    <p class="hero-sub">Want to save on bookkeeping fees for your existing business?</p>
  </section>

  <svg class="brand-arc" viewBox="0 0 368 82" preserveAspectRatio="none" aria-hidden="true">
    <path d="M0 0 H368 V4 Q184 100 0 4 Z" fill="#ffffff"/>
    <path d="M30 20 Q184 110 338 20 Q184 92 30 20 Z" fill="#ec1f27"/>
  </svg>
  <div class="brand">
    <span class="brand-dot"></span>
    <span class="brand-name">Tally Your Ledger Free</span>
  </div>

  <div class="offer-frame"></div>
  <p class="offer-lead"><span>You can now</span></p>
  <h2 class="offer-headline">SAVE 1000'S OFF</h2>
  <p class="offer-tail"><span>bookkeeping fees by Doing it Yourself.</span></p>

  <div class="details">
    <p>Using our Bookkeeper software you simply key in the<br>information as you go.</p>
    <p>We offer one on one training, backup and support.<br>We can assist you with BAS Preparation and Payrol Advice.</p>
  </div>

  <section class="modules">
    <h3 class="modules-title">ADD MODULES AS REQUIRED</h3>
    <div class="module module-pos">POINT OF<br>SALE MODULE</div>
    <div class="module module-jobs">JOBS<br>MANAGEMENT<br>MODULE</div>
    <div class="module module-web">WEBSITE<br>INTERGRATION<br>MODULE</div>
  </section>

  <p class="setup">FEE SET UP<br>ASSISTANCE AND TRAINING.</p>
  <p class="setup-cta">LETS GET THE BALL ROLLING</p>

  <footer class="contact-band">
    <div class="phone">
      <svg width="30" height="30" viewBox="0 0 30 30" aria-hidden="true">
        <circle cx="15" cy="15" r="15" fill="#ffe600"/>
        <path d="M10 7 l3 0 l1.5 5 l-2 1.5 q1.5 3.5 5 5 l1.5 -2 l5 1.5 l0 3 q-1 2 -3 2 q-7 -0.5 -12 -6.5 q-2.5 -3.5 -2 -7.5 q0.5 -1.5 3 -2 z" fill="#a3000d"/>
      </svg>
      <span>1300-642-815</span>
    </div>
    <div class="links">
      <span><svg width="11" height="11" viewBox="0 0 12 12" aria-hidden="true"><circle cx="6" cy="6" r="5" fill="none" stroke="#ffe600" stroke-width="1.3"/><path d="M1 6h10M6 1v10" stroke="#ffe600" stroke-width="1"/></svg>www.tylfr.com.au</span>
      <span><svg width="11" height="11" viewBox="0 0 12 12" aria-hidden="true"><circle cx="6" cy="6" r="6" fill="#ffe600"/><rect x="2.5" y="3.5" width="7" height="5" fill="none" stroke="#a3000d" stroke-width="1"/><path d="M2.5 3.5l3.5 3 3.5-3" fill="none" stroke="#a3000d" stroke-width="1"/></svg>admin@tylfr.com.au</span>
    </div>
  </footer>
</div>
</body>
</html>
```